Web site for Velmo Steadfast Advisory Pty. Ltd.

Create a modern website that is contemporary and appropriate for a business that is a provider of Consulting services to businesses. The LOGO is provided below. The consulting services offered are Supply Chain Management, 4th Party Logistics, Sales Coaching and training, HR services and training (i.e. Sexual Harassment and Bullying policies etc. ) , OH&S Training, Management mentoring, Business strategy and tactical consultations and Union related contract negotiations with award inclusion.

Target Market(s)

Importers, Exporters, Manufacturers, Freight Forwarders, Companies with large sales teams, warehouse operators

Industry/Entity Type

Business

Coding

Number of Pages Required

5+ page

Font styles to use
Serif
Sans Serif

Colors

Designer to choose colors to be used in the design.

Requirements
Must have
• Sky Line Photographs of Sydney and Manhattan, Pictures of people and teams in professional settings with tasteful clothing. Elements of both femininity and masculinity. People photos need to be diverse and include multiple nationalities, races and genders. Must have blog spot and also include the background info of the owners. Connectra pages includes.
Nice to have
• Would like to try both color and / or black and white.
Should not have
• Open

```html
<!DOCTYPE html>
<html lang="en">
<head>
<meta charset="utf-8">
<title>Velmo Steadfast Advisory</title>
<link href="https://fonts.googleapis.com/css2?family=Mulish:wght@400;600;700&family=Open+Sans:wght@400;600;700&display=swap" rel="stylesheet">
<style>
:root{
  --ink:#222;
  --dark:#262626;
  --panel:#2b2b2b;
  --text:#555;
  --muted:#777;
  --line:#ddd;
  --white:#fff;
  --sky1:#5d6672;
  --sky2:#a9a39a;
  --water:#4a5563;
}
*{margin:0;padding:0;box-sizing:border-box}
html,body{width:1200px;height:3403px;overflow:hidden}
body{position:relative;font-family:"Open Sans",Arial,sans-serif;color:var(--text);background:var(--white)}
.abs{position:absolute}
h1,h2,h3,h4{font-family:"Mulish",Arial,sans-serif;font-weight:600}
.btn{position:absolute;display:flex;align-items:center;justify-content:center;gap:6px;font-family:"Open Sans",Arial,sans-serif;font-size:13px;font-weight:600;letter-spacing:.5px;text-transform:uppercase}
.btn-light{border:2px solid var(--white);color:var(--white)}
.btn-dark{border:2px solid var(--ink);color:var(--ink)}

/* hero */
.hero{position:absolute;left:0;top:0;width:1200px;height:642px;background:linear-gradient(180deg,#3c434d 0%,var(--sky1) 30%,var(--sky2) 55%,#6b6a66 72%,var(--water) 82%,#3a4350 100%)}
.hero-shade{position:absolute;inset:0;background:rgba(0,0,0,.18)}
.brand{position:absolute;left:102px;top:28px;color:var(--white);font-family:"Mulish",Arial,sans-serif;font-weight:600;font-size:26px;line-height:1.1;width:260px}
.nav{position:absolute;left:490px;top:50px;display:flex;gap:33px;font-size:16px;color:var(--white);font-weight:600}
.nav .active{position:relative}
.nav .active::before{content:"";position:absolute;left:-6px;top:-50px;width:54px;height:7px;background:var(--white)}
.hero-title{position:absolute;left:0;top:265px;width:1200px;text-align:center;color:var(--white);font-size:44px;line-height:57px;font-weight:700;text-transform:uppercase}
.dots{position:absolute;left:555px;top:569px;display:flex;gap:9px}
.dots span{width:12px;height:12px;border-radius:50%;background:rgba(255,255,255,.75)}
.dots span:first-child{background:var(--white);box-shadow:0 0 0 2px rgba(255,255,255,.5)}

/* intro */
.intro-art{left:79px;top:703px;width:527px;height:272px;background:linear-gradient(180deg,#f4f4f4,#e4e4e4);border-radius:4px}
.intro-title{left:646px;top:725px;font-size:34px;color:var(--ink);font-weight:400}
.intro-copy{left:646px;top:792px;width:490px;font-size:15px;line-height:25px;color:var(--muted)}
.intro-copy p+p{margin-top:14px}

/* services */
.services{left:0;top:1084px;width:1200px;height:594px;background:var(--dark)}
.section-title{position:absolute;left:0;width:1200px;text-align:center;font-size:27px;letter-spacing:1px;text-transform:uppercase}
.services .section-title{top:52px;color:var(--white)}
.grid{position:absolute;left:98px;top:125px;display:grid;grid-template-columns:repeat(4,245px);grid-template-rows:192px 195px;gap:12px 9px}
.tile{border:2px solid #5a5a5a;display:flex;flex-direction:column;align-items:center;justify-content:center;color:var(--white);text-align:center;font-size:17px;line-height:25px;gap:16px}
.tile svg{width:56px;height:56px;stroke:var(--white);fill:none;stroke-width:2.4}

/* owners */
.owners .section-title{top:1714px;color:var(--ink)}
.owner{position:absolute;top:1780px;width:488px;height:220px;border:1px solid var(--line);box-shadow:0 2px 6px rgba(0,0,0,.08);background:var(--white)}
.owner-photo{position:absolute;left:40px;top:40px;width:132px;height:132px;border-radius:50%;background:linear-gradient(160deg,#d6d8da,#8a8f96)}
.owner-info{position:absolute;left:192px;top:28px;width:280px}
.owner-info h3{font-family:"Open Sans",Arial,sans-serif;font-size:19px;color:var(--ink);font-weight:600;text-transform:uppercase}
.owner-role{margin-top:12px;font-size:15px;color:var(--ink);line-height:22px}
.owner-bio{margin-top:8px;font-size:12.5px;line-height:19px;color:var(--muted)}

/* why */
.why-photo{left:0;top:2059px;width:601px;height:429px;background:linear-gradient(180deg,#dfe3e8 0%,#b8bec6 40%,#6e6560 75%,#4c4644 100%)}
.why{left:601px;top:2059px;width:599px;height:429px;background:var(--dark);color:var(--white)}
.why h2{position:absolute;left:61px;top:84px;font-size:27px;font-weight:600;text-transform:uppercase;letter-spacing:.5px}
.why-copy{position:absolute;left:61px;top:130px;width:470px;font-size:13.5px;line-height:22px}
.why-copy p+p{margin-top:12px}

/* blogs */
.blogs-title{left:102px;top:2522px;font-size:33px;color:var(--ink);text-transform:uppercase;font-weight:600}
.post-lead{left:102px;top:2583px;width:490px;height:358px;border:1px solid var(--line);background:var(--white)}
.post-lead .post-img{position:absolute;left:0;top:0;width:488px;height:210px;background:linear-gradient(180deg,#cfd3d8,#8f8a86)}
.date{position:absolute;left:22px;top:232px;width:52px;height:52px;border-radius:50%;background:var(--ink);color:var(--white);text-align:center;font-family:"Mulish",Arial,sans-serif;line-height:1}
.date b{display:block;font-size:20px;margin-top:9px}
.date small{font-size:11px;font-weight:700}
.post-lead h3{position:absolute;left:92px;top:228px;font-size:17px;color:var(--ink);font-weight:400}
.post-lead p{position:absolute;left:92px;top:256px;width:380px;font-size:11.5px;line-height:17px;color:var(--muted)}
.read{font-size:12px;font-weight:600;color:var(--ink);text-transform:uppercase}
.post-lead .read{position:absolute;left:92px;top:315px}
.post-side{left:608px;width:492px;height:174px;border:1px solid var(--line);background:var(--white)}
.post-side .post-img{position:absolute;left:0;top:0;width:225px;height:172px}
.post-side .body{position:absolute;left:249px;top:26px;width:225px}
.post-side h3{font-size:19px;color:var(--ink);font-weight:400}
.post-side p{margin-top:10px;font-size:11.5px;line-height:17px;color:var(--muted)}
.post-side .read{display:block;margin-top:6px}

/* footer */
.footer{left:0;top:3023px;width:1200px;height:380px;background:var(--dark);color:var(--white)}
.footer-brand{position:absolute;left:102px;top:90px;font-family:"Mulish",Arial,sans-serif;font-size:24px;font-weight:600;line-height:1.2;width:250px}
.fcol{position:absolute;top:55px}
.fcol h4{font-family:"Open Sans",Arial,sans-serif;font-size:19px;font-weight:600;padding-bottom:10px;border-bottom:1px solid #777}
.fcol ul{list-style:none;margin-top:12px;font-size:14.5px;line-height:32px}
.contact li{display:flex;align-items:center;gap:9px}
.contact svg{width:14px;height:14px;fill:var(--white)}
.socials{display:flex;gap:8px;margin-top:6px}
.socials span{width:28px;height:28px;border:2px solid var(--white);border-radius:50%}
.footer-rule{position:absolute;left:88px;top:311px;width:1024px;height:1px;background:#555}
.copyright{position:absolute;left:0;top:332px;width:1200px;text-align:center;font-size:13px;color:#bbb}
</style>
</head>
<body>

<header class="hero" role="img" aria-label="Photograph of the Sydney harbour skyline with the opera house and towers at dusk">
  <div class="hero-shade"></div>
  <div class="brand">Velmo Steadfast Advisory</div>
  <nav class="nav">
    <span class="active">Home</span><span>About Us</span><span>Services</span><span>Blog</span><span>Video</span><span>News</span><span>Contact</span>
  </nav>
  <h1 class="hero-title">Sales Coaching, Training<br>and HR Services</h1>
  <a class="btn btn-light" style="left:501px;top:395px;width:161px;height:43px">Read More</a>
  <div class="dots"><span></span><span></span><span></span><span></span></div>
</header>

<section class="intro">
  <div class="abs intro-art" role="img" aria-label="Line illustration of a consultant presenting charts among office and city elements"></div>
  <h2 class="abs intro-title">Velmo Steadfast Advisory</h2>
  <div class="abs intro-copy">
    <p>Sed ut perspiciatis unde omnis iste natus error sit voluptatem accusantium doloremque</p>
    <p>inventore veritatis et quasi architecto beatae vitae dicta sunt explicabo. Nemo enim ipsam voluptatem quia voluptas sit aspernatur aut odit aut fugit, sed quia consequunt</p>
  </div>
  <a class="btn btn-dark" style="left:646px;top:962px;width:139px;height:43px">Read More</a>
</section>

<section class="abs services">
  <h2 class="section-title">What We Do</h2>
  <div class="grid">
    <div class="tile"><svg viewBox="0 0 56 56"><circle cx="10" cy="28" r="5"/><circle cx="28" cy="12" r="5"/><circle cx="28" cy="44" r="5"/><circle cx="46" cy="28" r="5"/><circle cx="28" cy="28" r="4"/><path d="M14 25l10-9M14 31l10 9M32 16l10 9M32 40l10-9M28 17v7M28 32v7"/></svg>Supply Chain<br>Management</div>
    <div class="tile"><svg viewBox="0 0 56 56"><rect x="8" y="14" width="20" height="24"/><path d="M28 24h10l6 14H28M36 38v-30M36 38h14"/><circle cx="14" cy="44" r="4"/><circle cx="36" cy="44" r="4"/></svg>4th Party<br>Logistics</div>
    <div class="tile"><svg viewBox="0 0 56 56"><path d="M6 48h44M6 48V8"/><path d="M10 40l12-12 8 8 16-16M38 20h8v8"/></svg>Sales Coaching and<br>Training</div>
    <div class="tile"><svg viewBox="0 0 56 56"><circle cx="28" cy="18" r="7"/><circle cx="12" cy="22" r="5"/><circle cx="44" cy="22" r="5"/><path d="M16 44c0-10 6-14 12-14s12 4 12 14zM4 42c0-7 4-10 8-10M52 42c0-7-4-10-8-10"/></svg>HR services and<br>Training</div>
    <div class="tile"><svg viewBox="0 0 56 56"><rect x="6" y="8" width="32" height="22"/><path d="M12 24l8-8 6 5 8-9M14 30l-4 18M30 30l4 18"/><circle cx="46" cy="20" r="4"/><path d="M46 26v14M40 32h12M46 40l-4 8M46 40l4 8"/></svg>OH&amp;S Training</div>
    <div class="tile"><svg viewBox="0 0 56 56"><rect x="6" y="8" width="44" height="30" rx="2"/><path d="M22 38l-2 10M34 38l2 10M16 48h24"/></svg>Management<br>Mentoring</div>
    <div class="tile"><svg viewBox="0 0 56 56"><circle cx="28" cy="10" r="5"/><path d="M28 15v12M10 27h36M10 27v8M28 27v8M46 27v8"/><circle cx="10" cy="40" r="4"/><circle cx="28" cy="40" r="4"/><circle cx="46" cy="40" r="4"/></svg>Business Strategy &amp;<br>Tactical consultations</div>
    <div class="tile"><svg viewBox="0 0 56 56"><path d="M12 6h24l8 8v36H12z"/><path d="M18 18h18M18 26h18M18 34h12M22 44l4 3 8-8"/></svg>Union Related<br>Contract Negotiations</div>
  </div>
</section>

<section class="owners">
  <h2 class="section-title">Owners Profile</h2>
  <article class="owner" style="left:102px">
    <div class="owner-photo" role="img" aria-label="Portrait photo of the owner in a suit"></div>
    <div class="owner-info">
      <h3>Dale Ostrander</h3>
      <p class="owner-role">High Level Supply Chain Consulting<br>DOSTRANDER@MAILBOX.COM</p>
      <p class="owner-bio">I am a visionary and entrepreneur with a successful background in logistics and supply chain. I have been able to balance</p>
    </div>
  </article>
  <article class="owner" style="left:617px">
    <div class="owner-photo" role="img" aria-label="Portrait photo of the owner in a suit"></div>
    <div class="owner-info">
      <h3>Grant Hollis</h3>
      <p class="owner-role">Currently seeking new opportunities<br>grant@unionlink.org.au</p>
      <p class="owner-bio">Expertise in industrial relations, employee awareness campaigning, change management in small and large workforces</p>
    </div>
  </article>
</section>

<div class="abs why-photo" role="img" aria-label="Photograph of a seminar audience watching a presenter"></div>
<section class="abs why">
  <h2>Why Choose Us</h2>
  <div class="why-copy">
    <p>ullamcorper est eget tempor cursus neque mi consectetuer mi a ultricies massa est sed nisl Class aptent taciti</p>
    <p>sociosqu ad litora torquent per conubia nostra per inceptos h+ymenaeos ullamcorper est eget tempor cursus neque mi consectetuer mi a ultricies massa est sed nisl Class aptent taciti sociosqu ad litora torquent per conubia nostra</p>
  </div>
  <a class="btn btn-light" style="left:61px;top:299px;width:146px;height:41px">Read More
    <svg width="12" height="12" viewBox="0 0 12 12" fill="none" stroke="#fff" stroke-width="1.6"><circle cx="6" cy="6" r="5"/><path d="M5 3.5L7.5 6 5 8.5"/></svg></a>
</section>

<h2 class="abs blogs-title">Our Blogs</h2>
<article class="abs post-lead">
  <div class="post-img" role="img" aria-label="Photograph of a business meeting with a presenter at a whiteboard"></div>
  <div class="date"><b>01</b><small>JAN</small></div>
  <h3>Etiam est nunc venenatis in tristique</h3>
  <p>netus et malesuada fames ac turpis egestas Cras id elit Integer quis urna Ut ante enim dapibus malesuada fringilla eu condimen</p>
  <span class="read">Read More</span>
</article>
<article class="abs post-side" style="top:2583px">
  <div class="post-img" role="img" aria-label="Photograph of a conference hall audience" style="background:linear-gradient(180deg,#b9bcc2,#3f3c3c)"></div>
  <div class="body">
    <h3>Blog Title here</h3>
    <p>netus et malesuada fames ac turpis egestas Cras id elit Integer quis urna Ut ante enim dapibus malesuada fringilla eu condimen</p>
    <span class="read">Read More</span>
  </div>
</article>
<article class="abs post-side" style="top:2767px">
  <div class="post-img" role="img" aria-label="Photograph of business people shaking hands" style="background:linear-gradient(180deg,#dfe6ee,#5b6470)"></div>
  <div class="body">
    <h3>Blog Title here</h3>
    <p>netus et malesuada fames ac turpis egestas Cras id elit Integer quis urna Ut ante enim dapibus malesuada fringilla eu condimen</p>
    <span class="read">Read More</span>
  </div>
</article>

<footer class="abs footer">
  <div class="footer-brand">Velmo Steadfast Advisory</div>
  <div class="fcol" style="left:404px;width:140px">
    <h4>Company</h4>
    <ul><li>Home</li><li>About us</li><li>Our Services</li><li>What We Do</li></ul>
  </div>
  <div class="fcol" style="left:605px;width:140px">
    <h4>Resources</h4>
    <ul><li>Blogs</li><li>News</li><li>Our Solutions</li><li>Contact Us</li></ul>
  </div>
  <div class="fcol contact" style="left:785px;width:330px">
    <h4>Contact Us</h4>
    <ul>
      <li><svg viewBox="0 0 14 14"><path d="M7 0a5 5 0 0 0-5 5c0 4 5 9 5 9s5-5 5-9a5 5 0 0 0-5-5zm0 7a2 2 0 1 1 0-4 2 2 0 0 1 0 4z"/></svg>42 Harbour Lane Suite 5 Sydney NSW 2000</li>
      <li><svg viewBox="0 0 14 14"><path d="M3 0l3 3-2 2c1 2 3 4 5 5l2-2 3 3-2 3C6 14 0 8 0 3z"/></svg>555.010.4821</li>
      <li><svg viewBox="0 0 14 14"><path d="M0 2h14v10H0zM1 3l6 5 6-5" stroke="#262626" stroke-width="1"/></svg>info@velmoadvisory.com</li>
    </ul>
    <div class="socials" aria-label="Social links"><span></span><span></span><span></span><span></span></div>
  </div>
  <div class="footer-rule"></div>
  <p class="copyright">© 2018 Velmo Steadfast Advisory &nbsp;All right reserved</p>
</footer>

</body>
</html>
```